Lumoran signs for fridge and desk

I require 3 a4 designs very basic designs with single colour and easy to print. I have atached a style guide to see the fonts I used in my last three design. Please remember I'm printing in only one colour
PLease see the following link, of what I sell on quorbit. I will be selling this allong side these products.
https://www.quorbitshop.example/gp/item/K42H9XRDLM
Please see my competitors
https://www.quorbitshop.example/Planner-Magnetic-Calendar-Refrigerator-Container/dp/K7TQR2ZMWA/ref=sr_1_8?keywords=acrylic%2Bnote%2Bboard%2Brefrigerator%2Bdry%2Berase%2Bboard%2Bmagnetic%2Bclear&qid=1500000001&sr=8-8&th=1
and
https://www.quorbitshop.example/Magnetic-Acrylic-Calendar-Fridge-Refrigerator/dp/K9PWX4HNVE/ref=sr_1_4_sspa?keywords=acrylic+note+board+refrigerator+dry+erase+board+magnetic+clear&qid=1500000002&sr=8-4-spons&psc=1&spLa=UXhMbTNwZkRzWXZLcTJ3Rm5CaFRnSmRWZUx5UG1Sb1phSXVPY0F0TmJXa0dmWnNZeEhqUXJUbkxwVmRNZ0ViS2N5SXdBb0J1RnpQbVhoU2pOdFlxUmdDa1d2RHNMZUZuSHBaeEJtQ2tUZ1lqVnJRc0Vh
I'd like something more fun and different. But that can still be printed on Lumoran with one colour and be functional. A shopping list, a weekly planner(both that stick to a fridge) and a to do list that will sit on a desk or kitchen counter top.
PLease design
1st a4
Break into seven parts, with seven headings..... Monday to Sunday.... here customers will be able to write menus and upcoming events. I want this landcape
2nd a4
'Shopping List' is to be the heading
I want this landcape
3rd a4
'To Do List' is the only text I would like
I would like this portrat and lines marked and a check box on the left hand side
Remember I can only print on the acrylic with one colour. I want to be different from my competitors but I do want to be functional.
just a reminder. I can only print with one colour

```html
<!DOCTYPE html>
<html lang="en">
<head>
<meta charset="utf-8">
<title>Lumoran signs for fridge and desk</title>
<link rel="stylesheet" href="https://fonts.googleapis.com/css2?family=Cabin:wght@600&family=Libre+Baskerville&family=Open+Sans:wght@400&display=swap">
<style>
  :root {
    --ink: #000000;
    --paper: #ffffff;
    --muted: #8a8a8a;
    --frame: #3a3a3a;
  }
  html, body {
    margin: 0;
    padding: 0;
    width: 1200px;
    height: 1200px;
    overflow: hidden;
    background: var(--paper);
  }
  .sheet {
    display: block;
    width: 1200px;
    height: 1200px;
  }
  .sheet-frame { fill: var(--paper); stroke: var(--frame); stroke-width: 2; }
  .board-outline { fill: var(--paper); stroke: var(--ink); stroke-width: 1.6; }
  .mount-hole { fill: none; stroke: var(--ink); stroke-width: 1.6; }
  .day-tab { fill: var(--paper); stroke: var(--ink); stroke-width: 1.6; }
  .day-strip { fill: var(--ink); }
  .day-name {
    font-family: "Open Sans", Arial, sans-serif;
    font-size: 9px;
    fill: var(--paper);
    text-anchor: middle;
    dominant-baseline: middle;
  }
  .day-initial {
    font-family: "Libre Baskerville", "Times New Roman", serif;
    font-size: 58px;
    fill: var(--ink);
    text-anchor: middle;
  }
  .day-cell { fill: var(--paper); stroke: var(--ink); stroke-width: 1.2; }
  .cell-check { fill: none; stroke: var(--muted); stroke-width: 1.2; }
  .brand-name {
    font-family: "Cabin", "Gill Sans", sans-serif;
    font-weight: 600;
    fill: var(--ink);
  }
  .board-title {
    font-family: "Cabin", "Gill Sans", sans-serif;
    font-weight: 600;
    fill: var(--ink);
  }
  .write-line { stroke: var(--ink); stroke-width: 1.6; }
  .todo-box { fill: none; stroke: var(--ink); stroke-width: 1.8; }
</style>
</head>
<body>
<svg class="sheet" viewBox="0 0 1932 1932" xmlns="http://www.w3.org/2000/svg">
  <defs>
    <path id="landscape-board" d="M526 218 C650 230 760 163 838 163 C890 163 913 195 913 218 C913 260 862 430 862 453 L862 511 C862 534 913 730 913 745 C913 775 890 800 838 800 C760 800 650 733 526 745 C400 733 290 800 215 800 C165 800 140 775 140 745 C140 730 192 534 192 511 L192 453 C192 430 140 260 140 218 C140 195 165 163 215 163 C290 163 400 230 526 218 Z"/>
    <g id="landscape-holes">
      <circle class="mount-hole" cx="194" cy="218" r="17"/>
      <circle class="mount-hole" cx="859" cy="218" r="17"/>
      <circle class="mount-hole" cx="194" cy="745" r="17"/>
      <circle class="mount-hole" cx="859" cy="745" r="17"/>
    </g>
    <g id="cal-cell">
      <path class="day-cell" d="M0 0 H83 V44 Q83 64 63 64 H0 Z"/>
      <rect class="cell-check" x="2" y="2" width="9" height="9"/>
    </g>
    <g id="cal-column">
      <use href="#cal-cell" y="316"/>
      <use href="#cal-cell" y="384"/>
      <use href="#cal-cell" y="451"/>
      <use href="#cal-cell" y="519"/>
      <use href="#cal-cell" y="587"/>
      <use href="#cal-cell" y="655"/>
    </g>
    <path id="tab-shape" class="day-tab" d="M0 247 H83 V292 Q83 312 63 312 H0 Z"/>
    <g id="todo-row">
      <rect class="todo-box" x="0" y="0" width="16" height="16"/>
      <line class="write-line" x1="23" y1="14" x2="201" y2="14"/>
      <line class="write-line" x1="23" y1="30" x2="201" y2="30"/>
    </g>
  </defs>

  <rect class="sheet-frame" x="1" y="1" width="1930" height="1930"/>

  <!-- Weekly planner -->
  <g class="board board-planner">
    <use href="#landscape-board" class="board-outline"/>
    <use href="#landscape-holes"/>
    <text class="brand-name" font-size="17" transform="translate(214 372) rotate(-90)">Brindle Nook</text>

    <g class="planner-day" transform="translate(228 0)">
      <use href="#tab-shape"/><rect class="day-strip" x="0" y="247" width="16" height="65"/>
      <text class="day-name" transform="translate(8 279) rotate(-90)">SUNDAY</text>
      <text class="day-initial" x="49" y="302">S</text>
      <use href="#cal-column"/>
    </g>
    <g class="planner-day" transform="translate(314 0)">
      <use href="#tab-shape"/><rect class="day-strip" x="0" y="247" width="16" height="65"/>
      <text class="day-name" transform="translate(8 279) rotate(-90)">MONDAY</text>
      <text class="day-initial" x="49" y="302">M</text>
      <use href="#cal-column"/>
    </g>
    <g class="planner-day" transform="translate(401 0)">
      <use href="#tab-shape"/><rect class="day-strip" x="0" y="247" width="16" height="65"/>
      <text class="day-name" transform="translate(8 279) rotate(-90)">TUESDAY</text>
      <text class="day-initial" x="49" y="302">T</text>
      <use href="#cal-column"/>
    </g>
    <g class="planner-day" transform="translate(487 0)">
      <use href="#tab-shape"/><rect class="day-strip" x="0" y="247" width="16" height="65"/>
      <text class="day-name" font-size="8" transform="translate(8 279) rotate(-90)">WEDNESDY</text>
      <text class="day-initial" x="49" y="302">W</text>
      <use href="#cal-column"/>
    </g>
    <g class="planner-day" transform="translate(573 0)">
      <use href="#tab-shape"/><rect class="day-strip" x="0" y="247" width="16" height="65"/>
      <text class="day-name" transform="translate(8 279) rotate(-90)">THURSDAY</text>
      <text class="day-initial" x="49" y="302">T</text>
      <use href="#cal-column"/>
    </g>
    <g class="planner-day" transform="translate(659 0)">
      <use href="#tab-shape"/><rect class="day-strip" x="0" y="247" width="16" height="65"/>
      <text class="day-name" transform="translate(8 279) rotate(-90)">FRIDAY</text>
      <text class="day-initial" x="49" y="302">F</text>
      <use href="#cal-column"/>
    </g>
    <g class="planner-day" transform="translate(746 0)">
      <use href="#tab-shape"/><rect class="day-strip" x="0" y="247" width="16" height="65"/>
      <text class="day-name" transform="translate(8 279) rotate(-90)">SAURDAY</text>
      <text class="day-initial" x="49" y="302">S</text>
      <use href="#cal-column"/>
    </g>
  </g>

  <!-- Shopping list -->
  <g class="board board-shopping">
    <use href="#landscape-board" class="board-outline" transform="translate(907 0)"/>
    <use href="#landscape-holes" transform="translate(907 0)"/>
    <text class="board-title" x="1172" y="285" font-size="38">Shopping List</text>
    <text class="brand-name" x="1697" y="276" font-size="17" text-anchor="end">Brindle Nook</text>
    <g class="shopping-lines">
      <line class="write-line" x1="1169" x2="1697" y1="323" y2="323"/>
      <line class="write-line" x1="1169" x2="1697" y1="341.3" y2="341.3"/>
      <line class="write-line" x1="1169" x2="1697" y1="359.6" y2="359.6"/>
      <line class="write-line" x1="1169" x2="1697" y1="377.9" y2="377.9"/>
      <line class="write-line" x1="1169" x2="1697" y1="396.1" y2="396.1"/>
      <line class="write-line" x1="1169" x2="1697" y1="414.4" y2="414.4"/>
      <line class="write-line" x1="1169" x2="1697" y1="432.7" y2="432.7"/>
      <line class="write-line" x1="1169" x2="1697" y1="451" y2="451"/>
      <line class="write-line" x1="1169" x2="1697" y1="469.3" y2="469.3"/>
      <line class="write-line" x1="1169" x2="1697" y1="487.6" y2="487.6"/>
      <line class="write-line" x1="1169" x2="1697" y1="505.9" y2="505.9"/>
      <line class="write-line" x1="1169" x2="1697" y1="524.1" y2="524.1"/>
      <line class="write-line" x1="1169" x2="1697" y1="542.4" y2="542.4"/>
      <line class="write-line" x1="1169" x2="1697" y1="560.7" y2="560.7"/>
      <line class="write-line" x1="1169" x2="1697" y1="579" y2="579"/>
      <line class="write-line" x1="1169" x2="1697" y1="597.3" y2="597.3"/>
      <line class="write-line" x1="1169" x2="1697" y1="615.6" y2="615.6"/>
      <line class="write-line" x1="1169" x2="1697" y1="633.9" y2="633.9"/>
      <line class="write-line" x1="1169" x2="1697" y1="652.1" y2="652.1"/>
      <line class="write-line" x1="1169" x2="1697" y1="670.4" y2="670.4"/>
      <line class="write-line" x1="1169" x2="1697" y1="688.7" y2="688.7"/>
      <line class="write-line" x1="1169" x2="1697" y1="707" y2="707"/>
    </g>
  </g>

  <!-- To do list -->
  <g class="board board-todo">
    <path class="board-outline" d="M826 987 L883 987 C950 970 1050 940 1100 937 C1150 935 1173 965 1173 995 C1173 1080 1110 1200 1118 1320 C1110 1440 1173 1560 1173 1650 C1173 1680 1150 1707 1100 1707 C1050 1705 950 1675 883 1658 L826 1658 C760 1675 660 1705 610 1707 C560 1707 538 1680 538 1650 C538 1560 600 1440 594 1320 C600 1200 538 1080 538 995 C538 965 560 935 610 937 C660 940 760 970 826 987 Z"/>
    <circle class="mount-hole" cx="592" cy="988" r="17"/>
    <circle class="mount-hole" cx="1118" cy="988" r="17"/>
    <circle class="mount-hole" cx="592" cy="1654" r="17"/>
    <circle class="mount-hole" cx="1118" cy="1654" r="17"/>
    <text class="board-title" x="616" y="1060" font-size="40">To Do List</text>
    <text class="brand-name" x="1073" y="1057" font-size="17" text-anchor="end">Brindle Nook</text>
    <g class="todo-column">
      <use href="#todo-row" x="632" y="1117"/>
      <use href="#todo-row" x="632" y="1174.4"/>
      <use href="#todo-row" x="632" y="1231.8"/>
      <use href="#todo-row" x="632" y="1289.2"/>
      <use href="#todo-row" x="632" y="1346.6"/>
      <use href="#todo-row" x="632" y="1404"/>
      <use href="#todo-row" x="632" y="1461.4"/>
      <use href="#todo-row" x="632" y="1518.8"/>
      <use href="#todo-row" x="632" y="1576.2"/>
    </g>
    <g class="todo-column">
      <use href="#todo-row" x="876" y="1117"/>
      <use href="#todo-row" x="876" y="1174.4"/>
      <use href="#todo-row" x="876" y="1231.8"/>
      <use href="#todo-row" x="876" y="1289.2"/>
      <use href="#todo-row" x="876" y="1346.6"/>
      <use href="#todo-row" x="876" y="1404"/>
      <use href="#todo-row" x="876" y="1461.4"/>
      <use href="#todo-row" x="876" y="1518.8"/>
      <use href="#todo-row" x="876" y="1576.2"/>
    </g>
  </g>
</svg>
</body>
</html>
```